Simple, clean boat charter Banners

We need a variety of banner designs for our charter boat company. We provide boat trips to marlow shoals, beaches and snorkeling. You can see our site www.velmarotrips.com to get a better idea of our image.

We need the banner to be clean, simple and pleasing to the eye. The following ad dimensions we need are:

300 x 250
336 x 280
728 x 90
300 x 600
320 x 100

I've included a range of photos and logos to pic from.

Ignore the logo in all the photos. If a portion of the logo in the photo is in the banner, down worry. I will proved photos with the logo removed for the winning designs.

Please include a phrase, such as the following:
- Private Boat Charters to Marlow Shoals
- Private Boat Charters in Grand Cayman

If you can think of fun witty phrases, feel free to try them out. We are very open to creative ideas!! For example:
- Come visit the stingrays with us!
- Have you ever kissed a stingray?

Target Market(s)

Up-scale 30-50 year olds residing in North America

Industry/Entity Type

Tourism

Colors
3176b5
0655a3
85cae6
33a6d7
0592cd
cee9f5

Requirements
Nice to have
• Clean, Simple, Modern

```html
<!DOCTYPE html>
<html lang="en">
<head>
<meta charset="utf-8">
<title>Velmaro Trips – Banner Set</title>
<link href="https://fonts.googleapis.com/css2?family=Oswald:wght@300;400;600&display=swap" rel="stylesheet">
<style>
:root{
  --canvas:#8a8a8a;
  --navy:#0b0d22;
  --ink:#1b1f3f;
  --white:#ffffff;
  --header-top:#ffffff;
  --header-bottom:#d9d9dc;
  --orange-1:#ffc02a;
  --orange-2:#f08400;
  --btn-text:#2a1600;
  --sky:#7fb2dc;
  --lagoon-1:#2f8f7a;
  --lagoon-2:#14533f;
  --pool-1:#7fe3f5;
  --pool-2:#14a9d3;
  --sea-1:#2f6fc8;
  --sea-2:#36c3c8;
}
*{box-sizing:border-box;margin:0;padding:0}
html,body{width:1200px;height:1200px;overflow:hidden;background:var(--canvas)}
body{position:relative;font-family:'Oswald',sans-serif;color:var(--white)}
.banner{position:absolute;background:var(--navy);overflow:hidden}

/* photo areas */
.photo{position:absolute}
.ph-beach{background:linear-gradient(180deg,var(--sky) 0%,#c9d8e6 22%,#3d7a56 27%,var(--lagoon-1) 32%,var(--lagoon-2) 100%)}
.ph-lagoon{background:linear-gradient(90deg,var(--lagoon-2),var(--lagoon-1) 50%,var(--lagoon-2))}
.ph-snorkel{background:radial-gradient(circle at 60% 70%,var(--pool-1),var(--pool-2) 75%)}
.ph-boat{background:linear-gradient(180deg,var(--sea-1) 0%,#6fa6dd 28%,var(--sea-2) 42%,#1fb3c0 100%)}

/* logo */
.logo{position:absolute;top:0;left:0;background:linear-gradient(180deg,var(--header-top),var(--header-bottom));
  display:flex;flex-direction:column;align-items:center;justify-content:center;color:var(--ink);
  font-weight:400;letter-spacing:4px;line-height:1;text-align:center}
.logo span{display:block}

/* type */
.title{position:absolute;text-align:center;line-height:1;text-transform:uppercase;letter-spacing:-.5px}
.title span{display:block;white-space:nowrap}
.title .light{font-weight:300}
.title .bold{font-weight:600}
.tagline{position:absolute;text-align:center;font-weight:300;line-height:1.15;white-space:nowrap;letter-spacing:-.3px}

/* button */
.cta{position:absolute;display:flex;align-items:center;justify-content:center;gap:6px;
  background:linear-gradient(180deg,var(--orange-1),var(--orange-2));border-radius:3px;
  color:var(--btn-text);font-weight:400;text-transform:uppercase;letter-spacing:-.2px;white-space:nowrap}
.cta svg{flex:none}

/* 336x280 */
.sq{width:272px;height:226px}
.sq .logo{width:150px;height:62px;font-size:17px}
.sq .photo{right:0;top:0;bottom:0;width:130px;border-top-left-radius:36px 100%}
.sq .title{left:0;width:150px;top:70px;font-size:20px}
.sq .tagline{left:0;width:150px;top:148px;font-size:15px}
.sq .cta{left:18px;top:187px;width:108px;height:26px;font-size:14px}

/* 300x250 */
.md{width:256px;height:213px}
.md .logo{width:150px;height:58px;font-size:16px}
.md .photo{right:0;top:0;bottom:0;width:125px;border-top-left-radius:36px 100%}
.md .title{left:0;width:130px;top:66px;font-size:18.5px}
.md .tagline{left:0;width:130px;top:138px;font-size:14px}
.md .cta{left:8px;top:175px;width:103px;height:24px;font-size:13px}

/* 300x600 */
.sky{width:240px;height:480px}
.sky .logo{width:240px;height:74px;font-size:22px;letter-spacing:6px}
.sky .photo{left:0;right:0;top:240px;bottom:0;border-top-left-radius:100% 58px}
.sky .title{left:0;width:240px;top:84px;font-size:27px}
.sky .tagline{left:0;width:240px;top:176px;font-size:14.5px}
.sky .cta{left:64px;top:203px;width:108px;height:26px;font-size:14px}

/* 728x90 */
.lb{width:582px;height:72px}
.lb .logo{width:126px;height:72px;font-size:16px}
.lb .photo{left:340px;right:0;top:0;bottom:0;border-top-left-radius:30px 100%}
.lb .title{left:128px;width:200px;top:6px;font-size:19px;line-height:1.1}
.lb .tagline{left:128px;width:200px;top:50px;font-size:14px;line-height:1}
.lb .cta{left:476px;top:23px;width:104px;height:26px;font-size:14px}

/* 320x100 */
.mob{width:255px;height:80px}
.mob .photo{left:120px;right:0;top:0;bottom:0;border-top-left-radius:26px 100%}
.mob .title{left:0;width:122px;top:9px;font-size:19px;line-height:1.05}
</style>
</head>
<body>

<svg width="0" height="0" style="position:absolute" aria-hidden="true">
  <symbol id="go" viewBox="0 0 12 12"><circle cx="6" cy="6" r="6" fill="#2a1600"/><path d="M3 6h5M6 3.6 8.4 6 6 8.4" stroke="#ffb21a" stroke-width="1.6" fill="none"/></symbol>
</svg>

<!-- 336x280 row -->
<div class="banner sq" style="left:146px;top:32px">
  <div class="photo ph-beach" role="img" aria-label="Shallow green lagoon with a swimmer snorkelling and a palm-lined shore"></div>
  <div class="logo"><span>VELMARO</span><span>TRIPS</span></div>
  <div class="title"><span class="light">Private Boat</span><span class="bold">Charters in</span><span class="bold">Grand Cayman</span></div>
  <div class="tagline">Come visit the<br>stingrays with us!</div>
  <div class="cta">Learn More <svg width="11" height="11"><use href="#go"/></svg></div>
</div>
<div class="banner sq" style="left:464px;top:32px">
  <div class="photo ph-snorkel" role="img" aria-label="Family in snorkel masks underwater in bright turquoise water"></div>
  <div class="logo"><span>VELMARO</span><span>TRIPS</span></div>
  <div class="title"><span class="light">Private Boat</span><span class="bold">Charters in</span><span class="bold">Grand Cayman</span></div>
  <div class="tagline">Come visit the<br>stingrays with us!</div>
  <div class="cta">Learn More <svg width="11" height="11"><use href="#go"/></svg></div>
</div>
<div class="banner sq" style="left:782px;top:32px">
  <div class="photo ph-boat" role="img" aria-label="White charter boat anchored in turquoise water under a blue sky"></div>
  <div class="logo"><span>VELMARO</span><span>TRIPS</span></div>
  <div class="title"><span class="light">Private Boat</span><span class="bold">Charters in</span><span class="bold">Grand Cayman</span></div>
  <div class="tagline">Come visit the<br>stingrays with us!</div>
  <div class="cta">Learn More <svg width="11" height="11"><use href="#go"/></svg></div>
</div>

<!-- 300x250 column -->
<div class="banner md" style="left:54px;top:333px">
  <div class="photo ph-beach" role="img" aria-label="Shallow green lagoon with a swimmer snorkelling and a palm-lined shore"></div>
  <div class="logo"><span>VELMARO</span><span>TRIPS</span></div>
  <div class="title"><span class="light">Private Boat</span><span class="bold">Charters in</span><span class="bold">Grand Cayman</span></div>
  <div class="tagline">Come visit the<br>stingrays with us!</div>
  <div class="cta">Learn More <svg width="10" height="10"><use href="#go"/></svg></div>
</div>
<div class="banner md" style="left:54px;top:562px">
  <div class="photo ph-snorkel" role="img" aria-label="Family in snorkel masks underwater in bright turquoise water"></div>
  <div class="logo"><span>VELMARO</span><span>TRIPS</span></div>
  <div class="title"><span class="light">Private Boat</span><span class="bold">Charters in</span><span class="bold">Grand Cayman</span></div>
  <div class="tagline">Come visit the<br>stingrays with us!</div>
  <div class="cta">Learn More <svg width="10" height="10"><use href="#go"/></svg></div>
</div>
<div class="banner md" style="left:54px;top:792px">
  <div class="photo ph-boat" role="img" aria-label="White charter boat anchored in turquoise water under a blue sky"></div>
  <div class="logo"><span>VELMARO</span><span>TRIPS</span></div>
  <div class="title"><span class="light">Private Boat</span><span class="bold">Charters in</span><span class="bold">Grand Cayman</span></div>
  <div class="tagline">Come visit the<br>stingrays with us!</div>
  <div class="cta">Learn More <svg width="10" height="10"><use href="#go"/></svg></div>
</div>

<!-- 300x600 skyscrapers -->
<div class="banner sky" style="left:364px;top:295px">
  <div class="photo ph-beach" role="img" aria-label="Shallow green lagoon with a swimmer snorkelling and a palm-lined shore"></div>
  <div class="logo"><span>VELMARO</span><span>TRIPS</span></div>
  <div class="title"><span class="light">Private Boat</span><span class="bold">Charters in</span><span class="bold">Grand Cayman</span></div>
  <div class="tagline">Come visit the stingrays with us!</div>
  <div class="cta">Learn More <svg width="11" height="11"><use href="#go"/></svg></div>
</div>
<div class="banner sky" style="left:627px;top:294px">
  <div class="photo ph-snorkel" role="img" aria-label="Family in snorkel masks underwater in bright turquoise water"></div>
  <div class="logo"><span>VELMARO</span><span>TRIPS</span></div>
  <div class="title"><span class="light">Private Boat</span><span class="bold">Charters in</span><span class="bold">Grand Cayman</span></div>
  <div class="tagline">Come visit the stingrays with us!</div>
  <div class="cta">Learn More <svg width="11" height="11"><use href="#go"/></svg></div>
</div>
<div class="banner sky" style="left:893px;top:294px">
  <div class="photo ph-boat" role="img" aria-label="White charter boat anchored in turquoise water under a blue sky"></div>
  <div class="logo"><span>VELMARO</span><span>TRIPS</span></div>
  <div class="title"><span class="light">Private Boat</span><span class="bold">Charters in</span><span class="bold">Grand Cayman</span></div>
  <div class="tagline">Come visit the stingrays with us!</div>
  <div class="cta">Learn More <svg width="11" height="11"><use href="#go"/></svg></div>
</div>

<!-- 728x90 leaderboards -->
<div class="banner lb" style="left:430px;top:807px">
  <div class="photo ph-snorkel" role="img" aria-label="Family in snorkel masks underwater in bright turquoise water"></div>
  <div class="logo"><span>VELMARO</span><span>TRIPS</span></div>
  <div class="title"><span class="bold">Private Boat Charters</span><span class="light">in Grand Cayman</span></div>
  <div class="tagline">Come visit the stingrays with us!</div>
  <div class="cta">Learn More <svg width="11" height="11"><use href="#go"/></svg></div>
</div>
<div class="banner lb" style="left:430px;top:898px">
  <div class="photo ph-lagoon" role="img" aria-label="Swimmers snorkelling over a green lagoon"></div>
  <div class="logo"><span>VELMARO</span><span>TRIPS</span></div>
  <div class="title"><span class="bold">Private Boat Charters</span><span class="light">in Grand Cayman</span></div>
  <div class="tagline">Come visit the stingrays with us!</div>
  <div class="cta">Learn More <svg width="11" height="11"><use href="#go"/></svg></div>
</div>
<div class="banner lb" style="left:431px;top:985px">
  <div class="photo ph-boat" role="img" aria-label="White charter boat anchored in turquoise water under a blue sky"></div>
  <div class="logo"><span>VELMARO</span><span>TRIPS</span></div>
  <div class="title"><span class="bold">Private Boat Charters</span><span class="light">in Grand Cayman</span></div>
  <div class="tagline">Come visit the stingrays with us!</div>
  <div class="cta">Learn More <svg width="11" height="11"><use href="#go"/></svg></div>
</div>

<!-- 320x100 mobile -->
<div class="banner mob" style="left:180px;top:1092px">
  <div class="photo ph-boat" role="img" aria-label="White charter boat anchored in turquoise water under a blue sky"></div>
  <div class="title"><span class="light">Private Boat</span><span class="bold">Charters in</span><span class="bold">Grand Cayman</span></div>
</div>
<div class="banner mob" style="left:476px;top:1092px">
  <div class="photo ph-snorkel" role="img" aria-label="Family in snorkel masks underwater in bright turquoise water"></div>
  <div class="title"><span class="light">Private Boat</span><span class="bold">Charters in</span><span class="bold">Grand Cayman</span></div>
</div>
<div class="banner mob" style="left:773px;top:1092px">
  <div class="photo ph-lagoon" role="img" aria-label="Swimmers snorkelling over a green lagoon"></div>
  <div class="title"><span class="light">Private Boat</span><span class="bold">Charters in</span><span class="bold">Grand Cayman</span></div>
</div>

</body>
</html>
```